Halvern Dental website redesign

We need a redesign for a website: myhalverndental.com.

I already created a video going over what exactly is needed in the design.

See Video here: https://files.quorvane.com/file/d/8xKpQ2mWn4TzLrV7bHsYcE3jFuGaD6oN1/view?usp=sharing

review badge (plain shape) Slide shown in Video: https://slides.quorvane.com/presentation/d/7RtW2yQnXbVc4LmPz9KsHdJf3GaE8oUi6TeYqNvB5wZx/edit?usp=sharing
Updates

Holidays in India so we did not get enough design entries or quality.

Target Market(s)

Dentistry

Industry/Entity Type

Dentistry

Number of Pages Required

1 page

Colors
0094D4
00A9DD
6FCCEA
C7EBF8
E9F6FB
00AB8E
00BBA5
67D7C9
C6EFE9
E9F9F6

Requirements
Must have
• See 13 min video link in description - shows what to do.

```html
<!DOCTYPE html>
<html lang="en">
<head>
<meta charset="UTF-8">
<title>Halvern Dental</title>
<link rel="stylesheet" href="https://fonts.googleapis.com/css2?family=Roboto:wght@400;500;700&family=Playball&display=swap">
<style>
:root{
  --green:#5aab2e;
  --green-dark:#4a9624;
  --blue:#22aed4;
  --blue-deep:#0094d4;
  --sky:#e8f6fb;
  --ink:#222;
  --muted:#666;
  --line:#cfcfcf;
  --white:#fff;
}
*{box-sizing:border-box;margin:0;padding:0}
html,body{width:1200px;height:4511px;overflow:hidden;background:var(--white)}
body{position:relative;font-family:'Roboto',Arial,sans-serif;color:var(--ink)}
.abs{position:absolute}
.script{font-family:'Playball',cursive;font-weight:400}
.btn{position:absolute;display:flex;align-items:center;justify-content:center;background:var(--green);color:var(--white);font-size:12px;font-weight:700;text-transform:uppercase;border-radius:22px;letter-spacing:.2px}

/* header */
.site-header{position:absolute;left:0;top:0;width:1200px;height:88px;background:var(--white)}
.brand{position:absolute;left:143px;top:24px;display:flex;align-items:center;gap:10px;color:var(--green);font-size:26px;font-weight:500}
.brand-dot{width:16px;height:16px;border-radius:50%;background:var(--blue)}
.phone{position:absolute;left:415px;top:24px;display:flex;align-items:center;gap:12px;font-size:24px;font-weight:700;color:var(--ink)}
.phone span{color:var(--green)}
.hdr-btn{top:20px;height:40px;font-size:11px;font-weight:500}
.main-nav{position:absolute;left:0;top:88px;width:1200px;height:52px;background:var(--green);display:flex;padding-left:143px}
.main-nav a{display:flex;align-items:center;padding:0 16px;color:var(--white);font-size:13px;font-weight:500;text-decoration:none;text-transform:uppercase}
.main-nav a.active{background:var(--blue)}

/* hero */
.hero{position:absolute;left:0;top:140px;width:1200px;height:820px}
.hero-title{position:absolute;left:143px;top:92px;font-size:70px;line-height:70px;color:#1d1d1d}
.hero-sub{position:absolute;left:143px;top:343px;font-size:19px;line-height:29px;color:#333}
.hero-dots{position:absolute;left:1126px;top:248px;display:flex;flex-direction:column;gap:10px}
.hero-dots i{width:7px;height:7px;border-radius:50%;background:var(--white)}
.hero-dots i.on{background:var(--blue)}

/* headings */
.sec-title{position:absolute;left:0;width:1200px;text-align:center;font-size:64px;color:var(--green)}
.sec-title em{font-style:normal;color:var(--blue)}

/* team */
.doctor{position:absolute;width:300px;text-align:center}
.doc-ring{width:240px;height:240px;margin:0 auto;border:3px solid var(--green);border-radius:50%;display:flex;align-items:center;justify-content:center}
.doc-photo{width:190px;height:190px;border-radius:50%;background:radial-gradient(circle at 50% 45%,#8a6a57,#3c3431 70%)}
.doc-name{margin-top:30px;font-size:20px;font-weight:500;text-transform:uppercase}
.doc-bio{margin:20px auto 0;width:245px;font-size:12px;line-height:22px;color:var(--muted)}

/* services */
.services{position:absolute;left:0;top:1722px;width:1200px;height:528px;background:var(--sky)}
.svc{position:absolute;top:218px;width:216px;height:195px;background:var(--white);box-shadow:0 2px 6px rgba(0,0,0,.15);text-align:center}
.svc svg{margin-top:22px}
.svc p{margin-top:18px;font-size:15px;font-weight:500;text-transform:uppercase}
.arrow-round{position:absolute;top:298px;width:44px;height:44px;border:1.5px solid #555;border-radius:50%;display:flex;align-items:center;justify-content:center}

/* testimonials */
.avatar{position:absolute;left:548px;top:2450px;width:105px;height:105px;border-radius:50%;background:radial-gradient(circle at 50% 50%,#c9a891,#7d9a6e 75%)}
.quote{position:absolute;left:250px;top:2590px;width:700px;text-align:center;font-style:italic;font-size:16px;line-height:30px;color:#444}
.quote-name{position:absolute;left:0;width:1200px;top:2725px;text-align:center;font-size:20px;font-weight:500}
.quote-name span{color:var(--green);font-style:italic;font-weight:400}
.quote-date{position:absolute;left:0;width:1200px;top:2762px;text-align:center;font-size:13px;color:#444}
.badge{position:absolute;top:2818px;width:75px;height:48px;border-radius:4px}

/* difference */
.diff-photo{position:absolute;left:145px;top:2975px;width:456px;height:628px;border-radius:34px;background:linear-gradient(135deg,#d9c2a6,#a9795c 55%,#5d8aa8)}
.diff-card{position:absolute;left:497px;top:3030px;width:600px;height:540px;background:var(--white);border-radius:50px 0 0 0}
.diff-title{position:absolute;left:45px;top:65px;font-size:58px;line-height:62px;color:var(--green)}
.diff-title em{font-style:normal;color:var(--blue)}
.diff-text{position:absolute;left:45px;top:238px;width:490px;font-size:12px;line-height:21.7px;color:#555}

/* band */
.cta-band{position:absolute;left:0;top:3693px;width:1200px;height:317px;background:var(--blue);text-align:center;color:var(--white)}
.cta-band h2{position:absolute;left:0;width:1200px;top:75px;font-size:46px;color:var(--white)}
.cta-band p{position:absolute;left:0;width:1200px;top:145px;font-size:17px}

/* footer */
.ft-h{position:absolute;top:4080px;font-size:24px;font-weight:500}
.field{position:absolute;height:48px;border:1px solid var(--line);font-size:11px;color:#444;padding:0 20px;display:flex;align-items:center}
.hours{position:absolute;left:572px;top:4130px;list-style:none;font-size:11.5px;line-height:27.3px;color:#333}
.map{position:absolute;left:808px;top:4133px;width:242px;height:122px;border:1px solid var(--line);background:linear-gradient(135deg,#eef0ec,#dfe6de)}
.copy{position:absolute;left:0;width:1200px;top:4378px;text-align:center;font-size:12px;color:#333}
.social{position:absolute;left:526px;top:4440px;display:flex;gap:18px}
.social i{width:24px;height:24px;border-radius:50%;background:var(--green)}
.corner{position:absolute;left:1156px;top:4484px;font-size:10px;color:#555}
</style>
</head>
<body>

<header class="site-header">
  <div class="brand"><span class="brand-dot"></span>Halvern Dental</div>
  <div class="phone">
    <svg width="38" height="38" viewBox="0 0 38 38"><circle cx="19" cy="19" r="17" fill="none" stroke="var(--blue)" stroke-width="2.5"/><path d="M13 11c1-1 2-1 3 0l2 3c.6 1 .3 1.8-.5 2.5l-1 .8c.8 2 2.3 3.6 4.3 4.5l.8-1c.7-.8 1.5-1 2.4-.4l3 2c1 .7 1 1.8 0 2.8l-1.3 1.3c-1.5 1.5-5 .5-8.5-3s-5-7-3.5-8.5z" fill="var(--blue)"/></svg>
    <div><span>Phone :</span> (555) 018-4422</div>
  </div>
  <div class="btn hdr-btn" style="left:762px;width:164px">Schedule Online</div>
  <div class="btn hdr-btn" style="left:934px;width:123px;background:var(--blue)">Emergency</div>
</header>

<nav class="main-nav">
  <a class="active">About Us</a><a>Services</a><a>Financing</a><a>Testimonials</a><a>New Patient Visit</a><a>Specials</a><a>Contact Us</a><a>Blog</a>
</nav>

<section class="hero">
  <svg class="abs" style="left:0;top:0" width="1200" height="820" viewBox="0 0 1200 820" role="img" aria-label="Photo of a smiling couple embracing outdoors">
    <defs>
      <linearGradient id="heroTone" x1="0" y1="0" x2="1" y2="0">
        <stop offset="0" stop-color="#f1efea"/>
        <stop offset=".4" stop-color="#e3dbd0"/>
        <stop offset=".7" stop-color="#b78f74"/>
        <stop offset="1" stop-color="#7a5a48"/>
      </linearGradient>
    </defs>
    <path d="M0 0H1200V630C1000 790 700 850 480 785C300 735 130 640 0 480Z" fill="url(#heroTone)"/>
    <path d="M1200 630C1000 790 700 850 480 785C300 735 130 640 0 480" fill="none" stroke="var(--green)" stroke-width="8"/>
  </svg>
  <h1 class="hero-title script">Creating<br>Healthier<br>Smiles</h1>
  <p class="hero-sub">With Advanced Technology and<br>Affordable Treatment</p>
  <div class="btn" style="left:145px;top:438px;width:214px;height:42px">Book an Appointment</div>
  <div class="hero-dots"><i></i><i class="on"></i><i></i><i></i></div>
</section>

<h2 class="sec-title script" style="top:1020px">Our <em>Team</em></h2>

<div class="doctor" style="left:113px;top:1153px">
  <div class="doc-ring"><div class="doc-photo" role="img" aria-label="Portrait of Dr. Lena Varsh"></div></div>
  <h3 class="doc-name">Dr. Lena Varsh, DDS</h3>
  <p class="doc-bio">Dr. Lena Varsh is a graduate of the School of Dental Medicine at the University of Northfield, where she studied Cosmetic Dentistry,</p>
</div>
<div class="doctor" style="left:448px;top:1153px">
  <div class="doc-ring"><div class="doc-photo" role="img" aria-label="Portrait of Dr. Priya Donnel"></div></div>
  <h3 class="doc-name">Dr. Priya Donnel</h3>
  <p class="doc-bio">Dr. Donnel received her specialty training in Endodontics from Westbrook University. She graduated with a Master of Science in dentistry degree, in endodontics.</p>
</div>
<div class="doctor" style="left:785px;top:1153px">
  <div class="doc-ring"><div class="doc-photo" role="img" aria-label="Portrait of Dr. Ravi Kestrel"></div></div>
  <h3 class="doc-name">Dr. Ravi Kestrel</h3>
  <p class="doc-bio">Dr. Ravi Kestrel, DDS received his Bachelor of Dental Surgery Degree in 1999 from India. In 2000, he immigrated to the United States. After receiving</p>
</div>
<div class="btn" style="left:196px;top:1575px;width:135px;height:42px">Read More</div>
<div class="btn" style="left:530px;top:1575px;width:135px;height:42px">Read More</div>
<div class="btn" style="left:868px;top:1575px;width:135px;height:42px">Read More</div>

<section class="services">
  <h2 class="sec-title script" style="top:95px">Our <em>Services</em></h2>
  <div class="arrow-round" style="left:72px"><svg width="14" height="14" viewBox="0 0 14 14"><path d="M9 2L4 7l5 5" fill="none" stroke="#333" stroke-width="2"/></svg></div>
  <div class="arrow-round" style="left:1084px"><svg width="14" height="14" viewBox="0 0 14 14"><path d="M5 2l5 5-5 5" fill="none" stroke="#333" stroke-width="2"/></svg></div>

  <div class="svc" style="left:143px">
    <svg width="70" height="95" viewBox="0 0 70 95" fill="none" stroke="var(--green)" stroke-width="3"><path d="M10 18c0-12 50-12 50 0 0 8-6 12-8 14H18c-2-2-8-6-8-14z"/><rect x="25" y="34" width="20" height="8"/><path d="M22 48h26M24 58h22M26 68h18M29 78h12M33 88h4"/></svg>
    <p>Dental Implants</p>
  </div>
  <div class="svc" style="left:375px">
    <svg width="80" height="80" viewBox="0 0 80 80" fill="none" stroke="var(--green)" stroke-width="3"><rect x="4" y="8" width="72" height="26" rx="10"/><rect x="4" y="46" width="72" height="26" rx="10"/><path d="M18 8v26M32 8v26M48 8v26M62 8v26M18 46v26M32 46v26M48 46v26M62 46v26M4 40h72"/></svg>
    <p>Cosmetic Dentistry</p>
  </div>
  <div class="svc" style="left:607px">
    <svg width="80" height="90" viewBox="0 0 80 90" fill="none" stroke="var(--green)" stroke-width="3"><path d="M10 12c10-10 25-6 30-2 5-4 20-8 30 2 8 10 2 28-4 40-4 10-4 35-12 35-6 0-6-28-14-28s-8 28-14 28c-8 0-8-25-12-35C8 40 2 22 10 12z"/><path d="M6 30h68"/><rect x="18" y="24" width="10" height="12"/><rect x="35" y="24" width="10" height="12"/><rect x="52" y="24" width="10" height="12"/></svg>
    <p>Braces</p>
  </div>
  <div class="svc" style="left:840px">
    <svg width="70" height="95" viewBox="0 0 70 95" fill="none" stroke="var(--green)" stroke-width="3"><path d="M8 30C2 10 22 4 35 12 48 4 68 10 62 30c-2 8-6 10-8 12H16c-2-2-6-4-8-12z"/><rect x="22" y="44" width="26" height="8"/><path d="M25 58h20M27 68h16M30 78h10M33 88h4"/></svg>
    <p>Crowns</p>
  </div>
</section>

<h2 class="sec-title script" style="top:2340px">What Our Patients <em>Say About Us</em></h2>
<div class="avatar" role="img" aria-label="Photo of a smiling older couple"></div>
<svg class="abs" style="left:110px;top:2610px" width="36" height="66" viewBox="0 0 36 66"><path d="M34 2L3 33l31 31" fill="none" stroke="#999" stroke-width="2"/></svg>
<svg class="abs" style="left:1054px;top:2610px" width="36" height="66" viewBox="0 0 36 66"><path d="M2 2l31 31L2 64" fill="none" stroke="#999" stroke-width="2"/></svg>
<p class="quote">Lorem ipsum dolor sit amet, consectetur adipiscing elit, sed do eiusmod tempor incididunt ut labore et dolore magna aliquis ipsum suspendisse ultrices gravidaisus commodo viverraecenas accumsan lacus vel faciorem ipsum dolor sit ameonsectetur adipiscinged do eiusmod tempor incididunagna alpsum suspices lacus vel facilisis.</p>
<p class="quote-name">- Sam Rivera,<span>customer</span></p>
<p class="quote-date">October 16,2021</p>
<div class="badge" style="left:495px;background:#c4302b" role="img" aria-label="Review site rating badge"></div>
<span class="abs" style="left:585px;top:2832px;font-size:17px;font-weight:700">vs.</span>
<div class="badge" style="left:625px;background:#e8b923" role="img" aria-label="Search review rating badge"></div>

<div class="diff-photo" role="img" aria-label="Photo of two smiling teenage girls, one wearing braces"></div>
<div class="diff-card">
  <h2 class="diff-title script">Experience the Halvern<br><em>Dental Difference</em></h2>
  <p class="diff-text">Your smile is our #1 priority. At Halvern Dental, we provide affordable and expert dental solutions. Whether you are looking for a family dentist or have any emergency such as needing a root canal in Brookvale, we are here for you! We want to keep your teeth healthy inside and out. We don't just clean teeth and send you on your way, we want to get to know you.We accept most HMO and PPO insurances. We offer various financing options through SmileCredit, Lendwell and In-House Plans. To constantly strive to achieve the highest level of skills and modern techniques and equipment so we can provide our patients with the best that Dentistry has to offer at our dental office in Brookvale, Harbor County.</p>
</div>

<section class="cta-band">
  <h2 class="script">Committed to excellence in Oral Health Care</h2>
  <p>Free Exam and X-Rays for New Patients</p>
  <div class="btn" style="left:493px;top:195px;width:214px;height:42px">Book an Appointment</div>
</section>

<footer>
  <h3 class="ft-h" style="left:147px">Contact Form</h3>
  <div class="field" style="left:148px;top:4135px;width:163px">Enter Name</div>
  <div class="field" style="left:318px;top:4135px;width:163px">Enter Address</div>
  <div class="field" style="left:148px;top:4198px;width:333px">Phone</div>
  <div class="btn" style="left:148px;top:4262px;width:334px;height:42px">Book Your Free Consultation</div>

  <h3 class="ft-h" style="left:572px">Office Hours</h3>
  <ul class="hours">
    <li>Monday 10AM–7PM</li><li>Tuesday 10AM–7PM</li><li>Wednesday 9AM–6PM</li><li>Thursday 9AM–6PM</li><li>Friday 9AM–5PM</li><li>Saturday 9AM–1PM</li>
  </ul>

  <h3 class="ft-h" style="left:808px">Office Hours</h3>
  <div class="map" role="img" aria-label="Street map showing the office location"></div>

  <p class="copy">2021 MyHalvernDental.com.All rights reserved &nbsp;| &nbsp;Disclaimer &amp; Terms | Privacy Policy | Sitemap</p>
  <div class="social"><i></i><i></i><i></i><i></i></div>
  <span class="corner">C9</span>
</footer>

</body>
</html>
```